Garlic Farm for Farm Sales/Restaurant sales

Need a professional, but appealing to agriculture world. We are selling 27 kinds of Organic Garlic from a farm in Simla,CO. I have uploaded logo and business information-we are going to need a template, because I will need to use it for four separate people.
-We are trying to appeal to Farm to table restaurants
-As well as growers/farmers

Target Market(s)

Agriculture Sales/Restaurants-Organic

Industry/Entity Type

Agriculture

Contact Information for Business Card

Want it to look more unique then your average orbel mart card- I want it to look amazing

Font styles to use
Sans Serif

Colors
0455a3
ec1f27
fbed22
ffffff

Requirements
Must have
• Just be creative
Nice to have
• Colorful
Should not have
• plain

```html
<!DOCTYPE html>
<html lang="en">
<head>
<meta charset="utf-8">
<title>Summit Crest Garlic – Business Card</title>
<link rel="stylesheet" href="https://fonts.googleapis.com/css2?family=Open+Sans:wght@400;600;700&display=swap">
<style>
  :root {
    --navy: #0b2b5c;
    --red: #c0102e;
    --yellow: #fcd700;
    --white: #ffffff;
    --ink: #4a4a4a;
    --backdrop: #e9e6e1;
  }
  * { box-sizing: border-box; margin: 0; padding: 0; }
  html, body { width: 1200px; height: 987px; overflow: hidden; }
  body {
    background: var(--backdrop);
    font-family: "Open Sans", Arial, sans-serif;
    position: relative;
  }
  .card {
    position: absolute;
    left: 293px;
    width: 615px;
    height: 352px;
    overflow: hidden;
    box-shadow: 0 3px 10px rgba(0,0,0,.25);
  }
  .card--front { top: 130px; background: var(--white); }
  .card--back { top: 505px; background: var(--navy); }

  /* front */
  .faint-mark {
    position: absolute; left: -40px; top: 10px;
    width: 330px; height: 330px; border-radius: 50%;
    background: var(--red); opacity: .07;
  }
  .brand {
    position: absolute; left: 373px; top: 60px; width: 213px;
    display: flex; flex-direction: column; align-items: center; gap: 12px;
  }
  .brand__dot {
    width: 72px; height: 72px; border-radius: 50%; background: var(--red);
  }
  .brand__name {
    font-weight: 700; font-size: 27px; color: var(--navy);
    line-height: 1; text-align: center;
  }
  .person { position: absolute; left: 35px; top: 190px; }
  .person__name { font-size: 21px; font-weight: 600; color: var(--navy); letter-spacing: .3px; }
  .person__title { font-size: 15px; color: var(--red); margin-top: 2px; }
  .rule { position: absolute; left: 35px; right: 29px; top: 245px; height: 1px; background: var(--red); }
  .contacts { position: absolute; left: 35px; top: 256px; list-style: none; }
  .contacts li {
    display: flex; align-items: center; gap: 8px;
    font-size: 15px; color: var(--ink); height: 23.5px;
  }
  .contacts svg { width: 14px; height: 14px; fill: var(--navy); }
  .address {
    position: absolute; right: 29px; top: 279px;
    text-align: right; font-size: 15px; color: var(--ink); line-height: 23.5px;
  }
  .band { position: absolute; left: 0; bottom: 0; width: 615px; height: 13px; }

  /* back */
  .back__panel { position: absolute; left: 0; top: 0; width: 182px; height: 352px; background: var(--red); }
  .back__art {
    position: absolute; left: 14px; top: 8px; width: 292px; height: 338px;
    border-radius: 48% 48% 44% 44% / 58% 58% 40% 40%;
    background: radial-gradient(ellipse at 50% 65%, #ffe23a 0%, var(--yellow) 70%, #f2c800 100%);
  }
  .back__brand {
    position: absolute; left: 330px; top: 225px; width: 270px; text-align: center;
    color: var(--white); font-weight: 700; font-size: 28px; line-height: 1;
  }
  .social { position: absolute; left: 421px; top: 316px; display: flex; gap: 4px; }
  .social span { width: 20px; height: 20px; border-radius: 50%; border: 1.5px solid var(--white); }
</style>
</head>
<body>
  <section class="card card--front">
    <div class="faint-mark"></div>
    <div class="brand">
      <div class="brand__dot"></div>
      <div class="brand__name">Summit Crest Garlic</div>
    </div>
    <div class="person">
      <div class="person__name">OWEN HALE</div>
      <div class="person__title">CEO/FOUNDER</div>
    </div>
    <div class="rule"></div>
    <ul class="contacts">
      <li><svg viewBox="0 0 16 16"><path d="M3.5 1l2.5 3-1.5 2c1 2 3 4 5 5l2-1.5 3 2.5-1.5 2.5C7 14 2 9 1 2.5z"/></svg>555-014-2290</li>
      <li><svg viewBox="0 0 16 16"><path d="M1 3h14v10H1z M2 4l6 5 6-5" fill="var(--navy)"/><path d="M2.2 4.2l5.8 4.6 5.8-4.6" fill="none" stroke="#fff" stroke-width="1.2"/></svg>Nora@SCGarlic.com</li>
      <li><svg viewBox="0 0 16 16"><circle cx="8" cy="8" r="7"/><path d="M1 8h14M8 1c-3 3-3 11 0 14M8 1c3 3 3 11 0 14" fill="none" stroke="#fff" stroke-width="1"/></svg>www.SCGarlic.com</li>
    </ul>
    <div class="address">P.O. Box 48 Larkfield<br>CO&nbsp;&nbsp;80899</div>
    <svg class="band" viewBox="0 0 615 13" preserveAspectRatio="none">
      <rect width="615" height="13" fill="var(--navy)"/>
      <polygon points="411,13 418,0 468,0 461,13" fill="var(--white)"/>
      <polygon points="414,13 421,0 466,0 459,13" fill="var(--red)"/>
      <polygon points="462,13 469,0 474,0 467,13" fill="var(--white)"/>
      <polygon points="470,13 477,0 538,0 531,13" fill="var(--white)"/>
      <polygon points="473,13 480,0 533,0 526,13" fill="var(--yellow)"/>
    </svg>
  </section>

  <section class="card card--back">
    <div class="back__panel"></div>
    <div class="back__art" role="img" aria-label="Large yellow garlic bulb illustration"></div>
    <div class="back__brand">Summit Crest Garlic</div>
    <div class="social"><span></span><span></span><span></span><span></span></div>
  </section>
</body>
</html>
```